Business Card for Willowcrest Terrain Advisors

We need a business card for Willowcrest Terrain Advisors. The company website address is provided below. The company logo is attached. We provide specialized permafrost services to the mining, transportation, and oil & gas industries. The card should be prepared for:
Dominic Halloway, PhD.
Willowcrest Terrain Advisors
PO Box 418529
Birch Hollow, Alaska 99612
Direct: +1-907-555-2964
Email: dhalloway@terrainadvisors-example.com
Website: www.willowcrestterrainadvisors-example.com

```html
<!DOCTYPE html>
<html lang="en">
<head>
<meta charset="utf-8">
<title>Willowcrest Terrain Advisors – Business Card</title>
<link href="https://fonts.googleapis.com/css2?family=Lato:wght@400;700;900&display=swap" rel="stylesheet">
<style>
  :root {
    --backdrop: #2b2b2b;
    --navy: #111921;
    --paper: #ffffff;
    --ink: #111921;
    --muted: #5b5f63;
    --silver: #b9bec3;
  }
  * { margin: 0; padding: 0; box-sizing: border-box; }
  html, body { width: 1200px; height: 875px; overflow: hidden; }
  body {
    background: var(--backdrop);
    font-family: "Lato", sans-serif;
    position: relative;
  }
  .card {
    position: absolute;
    left: 290px;
    width: 620px;
    height: 354px;
    border-radius: 22px;
    overflow: hidden;
  }
  .card-front { top: 48px; background: var(--navy); }
  .card-back { top: 473px; background: var(--paper); }

  .brand { display: flex; align-items: center; gap: 12px; }
  .brand-mark { width: 14px; height: 14px; flex: none; }
  .brand-name { font-weight: 900; text-transform: uppercase; letter-spacing: 0.06em; line-height: 1.1; }

  .card-front .brand {
    position: absolute; inset: 0; justify-content: center;
  }
  .card-front .brand-mark { background: var(--silver); width: 18px; height: 18px; }
  .card-front .brand-name { color: var(--silver); font-size: 30px; }

  .card-back .brand { position: absolute; left: 46px; top: 84px; }
  .card-back .brand-mark { background: var(--ink); }
  .card-back .brand-name { color: var(--ink); font-size: 17px; width: 230px; }

  .name-band {
    position: absolute; right: 0; top: 112px;
    width: 272px; height: 86px;
    background: var(--navy);
    color: var(--paper);
    display: flex; flex-direction: column; justify-content: center;
    padding-left: 26px;
  }
  .person-name { font-weight: 900; font-size: 17px; letter-spacing: 0.01em; text-transform: uppercase; }
  .person-company { font-size: 14px; margin-top: 3px; }

  .accent-bar {
    position: absolute; left: 0; top: 232px;
    width: 7px; height: 76px; background: var(--navy);
  }

  .contact-list {
    position: absolute; left: 46px; top: 216px;
    list-style: none; color: var(--muted); font-size: 13.5px; line-height: 1.45;
  }
  .contact-list li { display: flex; gap: 12px; align-items: flex-start; }
  .contact-list svg { width: 13px; height: 13px; margin-top: 3px; flex: none; fill: var(--ink); }
  .contact-list .no-icon { padding-left: 25px; }
</style>
</head>
<body>
  <section class="card card-front">
    <div class="brand">
      <span class="brand-mark"></span>
      <span class="brand-name">Willowcrest Terrain Advisors</span>
    </div>
  </section>

  <section class="card card-back">
    <div class="brand">
      <span class="brand-mark"></span>
      <span class="brand-name">Willowcrest Terrain Advisors</span>
    </div>

    <div class="name-band">
      <p class="person-name">Dominic Halloway, PhD</p>
      <p class="person-company">Willowcrest Terrain Advisors</p>
    </div>

    <span class="accent-bar"></span>

    <ul class="contact-list">
      <li>
        <svg viewBox="0 0 24 24"><path d="M12 2a7 7 0 0 0-7 7c0 5 7 13 7 13s7-8 7-13a7 7 0 0 0-7-7zm0 9.5A2.5 2.5 0 1 1 12 6.5a2.5 2.5 0 0 1 0 5z"/></svg>
        <span>PO Box 418529</span>
      </li>
      <li class="no-icon"><span>Birch Hollow, Alaska 99612</span></li>
      <li>
        <svg viewBox="0 0 24 24"><path d="M6.6 10.8a15.1 15.1 0 0 0 6.6 6.6l2.2-2.2a1 1 0 0 1 1-.25 11.4 11.4 0 0 0 3.6.57 1 1 0 0 1 1 1V20a1 1 0 0 1-1 1A17 17 0 0 1 3 4a1 1 0 0 1 1-1h3.5a1 1 0 0 1 1 1c0 1.25.2 2.45.57 3.57a1 1 0 0 1-.25 1z"/></svg>
        <span>+1-907-555-2964</span>
      </li>
      <li>
        <svg viewBox="0 0 24 24"><path d="M2 5h20v14H2z M2 5l10 8 10-8" fill="none" stroke="#111921" stroke-width="2"/><path d="M2 5h20l-10 8z"/></svg>
        <span>dhalloway@terrainadvisors-example.com</span>
      </li>
      <li>
        <svg viewBox="0 0 24 24"><circle cx="12" cy="12" r="9" fill="none" stroke="#111921" stroke-width="2"/><path d="M3 12h18M12 3c3 3 3 15 0 18M12 3c-3 3-3 15 0 18" fill="none" stroke="#111921" stroke-width="1.6"/></svg>
        <span>willowcrestterrainadvisors-example.com</span>
      </li>
    </ul>
  </section>
</body>
</html>
```